New book cover for existing E-Bike tour book

I would like to update the current design of my book "Pedelec Rides through the Hazelmark" (translation: Pedelec Rides through the Hazelmark) and make it more modern.

Existing Book:
Title: "Pedelec rides through the Hazelmark"
Subtitle: 40 eventful tours with nature and culture.
Info bar with three elements:
 Unique sights
 Cozy beer gardens
 The most beautiful bike paths

objectives:
- to make the design more modern
- to make it attractive for people who want to ride E-bike

Requirements for the new design:

1. All texts for title, subtitle and info bar should be kept.
Font, color and placement can be changed.

2. the 5 nature images below the title are optional: can be used, can be replaced, can be omitted

3. the background image is optional: can be used or can be replaced with a totally different background.

Target Market(s)

People who want to discover the "Odenwald" region with the E-Bike

Font styles to use
Sans Serif

Requirements
Must have
• all texts for title, subtitle and info bar should be kept.
Nice to have
• It would be nice to see two E-bike riders. Like on the original book cover but just bigger in size. The two E-Bike riders on the original cover are a bit small.

```html
<!DOCTYPE html>
<html lang="en">
<head>
<meta charset="utf-8">
<title>Pedelec Rides through the Hazelmark – Book Cover</title>
<link rel="stylesheet" href="https://fonts.googleapis.com/css2?family=Bebas+Neue&family=Open+Sans:wght@700&display=swap">
<style>
  :root {
    --backdrop: #dedfdf;
    --fog-light: #e4e6e6;
    --fog-mid: #b9bec1;
    --tree-grey: #8a8f91;
    --verge-brown: #7a5a48;
    --road-mid: #58636e;
    --road-dark: #3a4550;
    --road-deep: #2b333d;
    --rider-dark: #1f2630;
    --title-blue: #1e7596;
    --ink-grey: #2f3336;
    --white: #ffffff;
  }
  * { margin: 0; padding: 0; box-sizing: border-box; }
  html, body {
    width: 1200px; height: 1013px; overflow: hidden;
    background: var(--backdrop);
  }
  .cover {
    position: absolute;
    left: 260px; top: 26px;
    width: 680px; height: 960px;
    overflow: hidden;
  }
  .cover-photo {
    position: absolute; inset: 0;
    background:
      radial-gradient(ellipse 30% 22% at 50% 50%, rgba(240,242,242,0.95), rgba(240,242,242,0) 75%),
      linear-gradient(90deg, rgba(120,126,128,0.55) 0%, rgba(120,126,128,0) 30%, rgba(120,126,128,0) 65%, rgba(122,90,72,0.45) 100%),
      linear-gradient(180deg, #cfd3d4 0%, var(--fog-light) 30%, var(--fog-mid) 55%, var(--road-mid) 66%, var(--road-dark) 82%, var(--road-deep) 100%);
  }
  .rider-photo {
    position: absolute;
    left: 305px; top: 385px;
    width: 100px; height: 355px;
    border-radius: 40px 40px 12px 12px;
    background: linear-gradient(180deg, rgba(31,38,48,0.85), rgba(31,38,48,0.7));
  }
  .cover-text { position: absolute; left: 0; right: 0; text-align: center; }
  .tagline {
    top: 28px;
    font-family: "Open Sans", sans-serif; font-weight: 700;
    font-size: 24px; line-height: 28px;
    color: var(--ink-grey); text-transform: uppercase;
  }
  .title-main, .title-link, .author {
    font-family: "Bebas Neue", sans-serif; font-weight: 400;
    text-transform: uppercase;
  }
  .title-main {
    font-size: 107px; line-height: 1; color: var(--title-blue);
    letter-spacing: 2px;
  }
  .title-top { top: 99px; }
  .title-bottom { top: 272px; }
  .title-link {
    top: 202px; font-size: 68px; line-height: 1;
    color: var(--white); letter-spacing: 2px;
    text-shadow: 0 2px 4px rgba(0,0,0,0.25);
  }
  .highlights {
    top: 758px; list-style: none;
    font-family: "Open Sans", sans-serif; font-weight: 700;
    font-size: 27px; line-height: 29px; color: var(--white);
  }
  .author {
    top: 882px; font-size: 50px; line-height: 1;
    color: var(--white); letter-spacing: 1px;
  }
</style>
</head>
<body>
  <article class="cover">
    <div class="cover-photo" role="img" aria-label="Misty forest road lined with bare autumn trees and a leaf-covered verge"></div>
    <div class="rider-photo" role="img" aria-label="Cyclist in dark kit and helmet riding away down the road, seen from behind"></div>
    <p class="cover-text tagline">40 eventful tours with nature and culture</p>
    <h1>
      <span class="cover-text title-main title-top">Pedelec Rides</span>
      <span class="cover-text title-link">through the</span>
      <span class="cover-text title-main title-bottom">Hazelmark</span>
    </h1>
    <ul class="cover-text highlights">
      <li>Unique sights</li>
      <li>Cozy beer gardens</li>
      <li>The most beautiful bike paths</li>
    </ul>
    <p class="cover-text author">Rainer Holzbach</p>
  </article>
</body>
</html>
```